" Fazer o calendário de parede conforme o anexo abaixo sendo que a parte para fazer o cabeçalho tem que ter a medida 41cm de comprimento por 11,5cm de altura "

```html
<!DOCTYPE html>
<html lang="pt-BR">
<head>
<meta charset="utf-8">
<title>Calendário de Parede 2024 — Vale Fresco Hortifruti</title>
<link href="https://fonts.googleapis.com/css2?family=Montserrat:wght@400;500;600&display=swap" rel="stylesheet">
<style>
  :root {
    --backdrop: #2b2624;
    --paper: #f7f6f3;
    --ink: #2e2e2e;
    --muted: #8a8a8a;
    --brand-green: #1f6b34;
    --orange: #f08a1c;
    --sun-band: #fbe3cf;
    --sun-ink: #e07a2a;
  }
  * { box-sizing: border-box; margin: 0; padding: 0; }
  html, body {
    width: 1200px; height: 1200px; overflow: hidden;
    background: var(--backdrop);
    font-family: "Montserrat", sans-serif;
    color: var(--ink);
  }
  .calendar-sheet {
    position: absolute; left: 190px; top: 20px;
    width: 820px; height: 1160px;
    background: var(--paper);
    display: flex; flex-direction: column;
  }
  .header {
    position: relative; height: 230px;
  }
  .header-photo {
    position: absolute; inset: 0;
    background: linear-gradient(100deg, #d9a548 0%, #f2a531 35%, #f07d1a 65%, #e8b532 100%);
  }
  .brand {
    position: absolute; left: 42px; top: 60px;
    display: flex; align-items: center; gap: 14px;
    background: var(--paper);
    padding: 16px 26px; border-radius: 6px;
  }
  .brand-dot { width: 22px; height: 22px; border-radius: 50%; background: var(--orange); }
  .brand-name {
    font-weight: 600; font-size: 30px; color: var(--brand-green); line-height: 1.1;
  }
  .months {
    flex: 1;
    display: grid; grid-template-columns: repeat(3, 1fr); grid-template-rows: repeat(4, 1fr);
    column-gap: 44px; padding: 26px 56px 10px;
  }
  .month-name {
    text-align: center; font-weight: 500; font-size: 19px; margin-bottom: 10px;
  }
  .weekdays, .days {
    display: grid; grid-template-columns: repeat(7, 1fr);
    text-align: center;
    background: linear-gradient(to right, transparent 85.71%, var(--sun-band) 85.71%);
  }
  .weekdays { font-size: 8px; color: var(--muted); padding: 3px 0; text-transform: lowercase; }
  .weekdays span:last-child { color: var(--sun-ink); }
  .days { font-size: 12px; line-height: 20px; font-weight: 500; }
  .footer-photo {
    height: 100px;
    background: linear-gradient(90deg, #f2a23a 0%, #3f7d36 30%, #f5c23c 55%, #f08a1c 85%, #f6a441 100%);
  }
</style>
</head>
<body>
<main class="calendar-sheet">
  <header class="header">
    <div class="header-photo" role="img" aria-label="Fotografia de laranjas empilhadas com uma laranja cortada ao meio sobre tábua de madeira"></div>
    <div class="brand"><span class="brand-dot"></span><span class="brand-name">Vale Fresco Hortifruti</span></div>
  </header>

  <section class="months">
    <div class="month"><h2 class="month-name">Janeiro</h2>
      <div class="weekdays"><span>seg</span><span>ter</span><span>qua</span><span>qui</span><span>sex</span><span>sáb</span><span>dom</span></div>
      <div class="days"><span style="grid-column-start:1">1</span><span>2</span><span>3</span><span>4</span><span>5</span><span>6</span><span>7</span><span>8</span><span>9</span><span>10</span><span>11</span><span>12</span><span>13</span><span>14</span><span>15</span><span>16</span><span>17</span><span>18</span><span>19</span><span>20</span><span>21</span><span>22</span><span>23</span><span>24</span><span>25</span><span>26</span><span>27</span><span>28</span><span>29</span><span>30</span><span>31</span></div>
    </div>
    <div class="month"><h2 class="month-name">Fevereiro</h2>
      <div class="weekdays"><span>seg</span><span>ter</span><span>qua</span><span>qui</span><span>sex</span><span>sáb</span><span>dom</span></div>
      <div class="days"><span style="grid-column-start:4">1</span><span>2</span><span>3</span><span>4</span><span>5</span><span>6</span><span>7</span><span>8</span><span>9</span><span>10</span><span>11</span><span>12</span><span>13</span><span>14</span><span>15</span><span>16</span><span>17</span><span>18</span><span>19</span><span>20</span><span>21</span><span>22</span><span>23</span><span>24</span><span>25</span><span>26</span><span>27</span><span>28</span><span>29</span></div>
    </div>
    <div class="month"><h2 class="month-name">Março</h2>
      <div class="weekdays"><span>seg</span><span>ter</span><span>qua</span><span>qui</span><span>sex</span><span>sáb</span><span>dom</span></div>
      <div class="days"><span style="grid-column-start:5">1</span><span>2</span><span>3</span><span>4</span><span>5</span><span>6</span><span>7</span><span>8</span><span>9</span><span>10</span><span>11</span><span>12</span><span>13</span><span>14</span><span>15</span><span>16</span><span>17</span><span>18</span><span>19</span><span>20</span><span>21</span><span>22</span><span>23</span><span>24</span><span>25</span><span>26</span><span>27</span><span>28</span><span>29</span><span>30</span><span>31</span></div>
    </div>
    <div class="month"><h2 class="month-name">Abril</h2>
      <div class="weekdays"><span>seg</span><span>ter</span><span>qua</span><span>qui</span><span>sex</span><span>sáb</span><span>dom</span></div>
      <div class="days"><span style="grid-column-start:1">1</span><span>2</span><span>3</span><span>4</span><span>5</span><span>6</span><span>7</span><span>8</span><span>9</span><span>10</span><span>11</span><span>12</span><span>13</span><span>14</span><span>15</span><span>16</span><span>17</span><span>18</span><span>19</span><span>20</span><span>21</span><span>22</span><span>23</span><span>24</span><span>25</span><span>26</span><span>27</span><span>28</span><span>29</span><span>30</span></div>
    </div>
    <div class="month"><h2 class="month-name">Maio</h2>
      <div class="weekdays"><span>seg</span><span>ter</span><span>qua</span><span>qui</span><span>sex</span><span>sáb</span><span>dom</span></div>
      <div class="days"><span style="grid-column-start:3">1</span><span>2</span><span>3</span><span>4</span><span>5</span><span>6</span><span>7</span><span>8</span><span>9</span><span>10</span><span>11</span><span>12</span><span>13</span><span>14</span><span>15</span><span>16</span><span>17</span><span>18</span><span>19</span><span>20</span><span>21</span><span>22</span><span>23</span><span>24</span><span>25</span><span>26</span><span>27</span><span>28</span><span>29</span><span>30</span><span>31</span></div>
    </div>
    <div class="month"><h2 class="month-name">Junho</h2>
      <div class="weekdays"><span>seg</span><span>ter</span><span>qua</span><span>qui</span><span>sex</span><span>sáb</span><span>dom</span></div>
      <div class="days"><span style="grid-column-start:6">1</span><span>2</span><span>3</span><span>4</span><span>5</span><span>6</span><span>7</span><span>8</span><span>9</span><span>10</span><span>11</span><span>12</span><span>13</span><span>14</span><span>15</span><span>16</span><span>17</span><span>18</span><span>19</span><span>20</span><span>21</span><span>22</span><span>23</span><span>24</span><span>25</span><span>26</span><span>27</span><span>28</span><span>29</span><span>30</span></div>
    </div>
    <div class="month"><h2 class="month-name">Julho</h2>
      <div class="weekdays"><span>seg</span><span>ter</span><span>qua</span><span>qui</span><span>sex</span><span>sáb</span><span>dom</span></div>
      <div class="days"><span style="grid-column-start:1">1</span><span>2</span><span>3</span><span>4</span><span>5</span><span>6</span><span>7</span><span>8</span><span>9</span><span>10</span><span>11</span><span>12</span><span>13</span><span>14</span><span>15</span><span>16</span><span>17</span><span>18</span><span>19</span><span>20</span><span>21</span><span>22</span><span>23</span><span>24</span><span>25</span><span>26</span><span>27</span><span>28</span><span>29</span><span>30</span><span>31</span></div>
    </div>
    <div class="month"><h2 class="month-name">Agosto</h2>
      <div class="weekdays"><span>seg</span><span>ter</span><span>qua</span><span>qui</span><span>sex</span><span>sáb</span><span>dom</span></div>
      <div class="days"><span style="grid-column-start:4">1</span><span>2</span><span>3</span><span>4</span><span>5</span><span>6</span><span>7</span><span>8</span><span>9</span><span>10</span><span>11</span><span>12</span><span>13</span><span>14</span><span>15</span><span>16</span><span>17</span><span>18</span><span>19</span><span>20</span><span>21</span><span>22</span><span>23</span><span>24</span><span>25</span><span>26</span><span>27</span><span>28</span><span>29</span><span>30</span><span>31</span></div>
    </div>
    <div class="month"><h2 class="month-name">Setembro</h2>
      <div class="weekdays"><span>seg</span><span>ter</span><span>qua</span><span>qui</span><span>sex</span><span>sáb</span><span>dom</span></div>
      <div class="days"><span style="grid-column-start:7">1</span><span>2</span><span>3</span><span>4</span><span>5</span><span>6</span><span>7</span><span>8</span><span>9</span><span>10</span><span>11</span><span>12</span><span>13</span><span>14</span><span>15</span><span>16</span><span>17</span><span>18</span><span>19</span><span>20</span><span>21</span><span>22</span><span>23</span><span>24</span><span>25</span><span>26</span><span>27</span><span>28</span><span>29</span><span>30</span></div>
    </div>
    <div class="month"><h2 class="month-name">Outubro</h2>
      <div class="weekdays"><span>seg</span><span>ter</span><span>qua</span><span>qui</span><span>sex</span><span>sáb</span><span>dom</span></div>
      <div class="days"><span style="grid-column-start:2">1</span><span>2</span><span>3</span><span>4</span><span>5</span><span>6</span><span>7</span><span>8</span><span>9</span><span>10</span><span>11</span><span>12</span><span>13</span><span>14</span><span>15</span><span>16</span><span>17</span><span>18</span><span>19</span><span>20</span><span>21</span><span>22</span><span>23</span><span>24</span><span>25</span><span>26</span><span>27</span><span>28</span><span>29</span><span>30</span><span>31</span></div>
    </div>
    <div class="month"><h2 class="month-name">Novembro</h2>
      <div class="weekdays"><span>seg</span><span>ter</span><span>qua</span><span>qui</span><span>sex</span><span>sáb</span><span>dom</span></div>
      <div class="days"><span style="grid-column-start:5">1</span><span>2</span><span>3</span><span>4</span><span>5</span><span>6</span><span>7</span><span>8</span><span>9</span><span>10</span><span>11</span><span>12</span><span>13</span><span>14</span><span>15</span><span>16</span><span>17</span><span>18</span><span>19</span><span>20</span><span>21</span><span>22</span><span>23</span><span>24</span><span>25</span><span>26</span><span>27</span><span>28</span><span>29</span><span>30</span></div>
    </div>
    <div class="month"><h2 class="month-name">Dezembro</h2>
      <div class="weekdays"><span>seg</span><span>ter</span><span>qua</span><span>qui</span><span>sex</span><span>sáb</span><span>dom</span></div>
      <div class="days"><span style="grid-column-start:7">1</span><span>2</span><span>3</span><span>4</span><span>5</span><span>6</span><span>7</span><span>8</span><span>9</span><span>10</span><span>11</span><span>12</span><span>13</span><span>14</span><span>15</span><span>16</span><span>17</span><span>18</span><span>19</span><span>20</span><span>21</span><span>22</span><span>23</span><span>24</span><span>25</span><span>26</span><span>27</span><span>28</span><span>29</span><span>30</span><span>31</span></div>
    </div>
  </section>

  <footer class="footer-photo" role="img" aria-label="Fotografia de laranjas e folhas verdes na base do calendário"></footer>
</main>
</body>
</html>
```